Hush And Look Through Poster for Harbourline Stack Keepers

Task Description
I am the Vice President of Advocacy for the Harbourline Stack Keepers Association. I am looking to have a set of posters made for HALT (Hush And Look Through) in October. HALT is a time when all school children in BC are encouraged to Hush And Look Through for 15-20 minutes at some point in their day.

I would like to get a set of 2 digital posters designed (if possible it would be nice to have the option to print to both 11x17 and 8.5x 11 paper). We need a poster that is high school (Grade 8-12) appropriate and one that is elementary (Grade k-7) appropriate. Both posters need to be replicated in French. All posters need to have the KEU logo on them as well as the Harbourline Stack Keepers Association Logo.

My budget is not huge (whose is?), but we are flexible and open with design. We want posters that appeal to the age groups they are designed for and that promote reading. We would require the digital copy by August 20. Schools will arrange for their own printing as distribution to all the schools in BC is laborious.

Each poster needs to have the following information:

-Hush And Look Through (HALT)
- A Blank Spot that we can add a date to
-the logo for the KEU (attached)
-the logo for the HSKA (attached)- the logos do not have to be large.

Industry/Entity Type

Teacher

Font styles to use
Serif

Requirements
Must have
• -Hush And Look Through (HALT)
• - A Blank Spot that we can add a date to
• -the logo for the KEU (attached)
• -the logo for the HSKA (attached)- the logos do not have to be large.
Nice to have
• Clear Bright Colours
• I have attached last year's posters to give an idea of what we are interested in.

```html
<!DOCTYPE html>
<html lang="en">
<head>
<meta charset="utf-8">
<title>HALT Poster – Harbourline Stack Keepers Association</title>
<link rel="stylesheet" href="https://fonts.googleapis.com/css2?family=Anton&family=Lato:wght@700;900&family=Righteous&display=swap">
<style>
  :root {
    --ink: #111111;
    --paper: #ffffff;
    --mist: #ececec;
    --leaf: #1f6a1c;
    --leaf-bright: #2f9e2a;
    --sun: #ffe400;
    --shelf-warm: #b58a5c;
    --shelf-light: #e9e2d6;
    --sweater: #f2c22a;
  }
  * { box-sizing: border-box; margin: 0; padding: 0; }
  html, body { width: 900px; height: 1200px; overflow: hidden; background: var(--paper); }
  .poster {
    position: relative;
    width: 900px;
    height: 1200px;
    overflow: hidden;
    background: var(--paper);
    font-family: "Lato", sans-serif;
  }
  .hero-photo {
    position: absolute;
    left: 0; top: 0;
    width: 900px; height: 600px;
    background:
      linear-gradient(to bottom, rgba(255,255,255,0) 60%, var(--paper) 100%),
      linear-gradient(to right, rgba(255,255,255,0.85) 0%, rgba(255,255,255,0.2) 35%, rgba(255,255,255,0) 55%),
      radial-gradient(ellipse 180px 300px at 690px 420px, var(--sweater) 0%, rgba(242,194,42,0) 100%),
      linear-gradient(90deg, var(--shelf-light) 0%, var(--shelf-warm) 50%, #8a6a48 100%);
  }
  .association-mark {
    position: absolute;
    left: 60px; top: 130px;
    font-family: "Lato", sans-serif;
    font-weight: 900;
    font-size: 120px;
    line-height: 1;
    color: var(--ink);
    letter-spacing: 2px;
  }
  .swoosh { position: absolute; left: 0; top: 0; }
  .headline {
    position: absolute;
    left: 0; width: 900px;
    text-align: center;
  }
  .headline-main {
    top: 625px;
    font-family: "Anton", sans-serif;
    font-size: 92px;
    line-height: 1;
    color: var(--ink);
    letter-spacing: 1px;
  }
  .headline-rule {
    position: absolute;
    left: 115px; top: 737px;
    width: 670px; height: 2px;
    background: var(--ink);
  }
  .headline-sub {
    top: 748px;
    font-family: "Righteous", sans-serif;
    font-size: 82px;
    line-height: 1;
    color: var(--leaf-bright);
    letter-spacing: 3px;
  }
  .union-mark {
    position: absolute;
    left: 70px; top: 1010px;
    font-family: "Lato", sans-serif;
    font-weight: 900;
    font-size: 64px;
    line-height: 1;
    color: var(--ink);
  }
  .event-name {
    position: absolute;
    right: 55px; top: 975px;
    font-weight: 900;
    font-size: 96px;
    line-height: 1;
    color: var(--leaf);
    text-align: right;
  }
  .event-date {
    position: absolute;
    right: 55px; top: 1090px;
    font-weight: 900;
    font-size: 62px;
    line-height: 1;
    color: var(--ink);
    text-align: right;
  }
  .event-date .date-blank { color: var(--leaf); }
</style>
</head>
<body>
  <main class="poster">
    <div class="hero-photo" role="img" aria-label="Smiling student in a yellow cardigan holding a stack of colourful books in front of blurred library shelves"></div>

    <div class="association-mark">HSKA</div>

    <svg class="swoosh" width="900" height="1200" viewBox="0 0 900 1200" aria-hidden="true">
      <path d="M0 690 C 220 930 520 990 900 770 L 900 1200 L 0 1200 Z" fill="var(--leaf-bright)"/>
      <path d="M0 720 C 220 955 520 1010 900 800 L 900 1200 L 0 1200 Z" fill="var(--ink)"/>
      <path d="M0 733 C 220 968 520 1022 900 814 L 900 1200 L 0 1200 Z" fill="var(--sun)"/>
      <path d="M200 1200 C 380 1020 600 930 900 895 L 900 1200 Z" fill="var(--ink)"/>
      <path d="M222 1200 C 400 1030 610 945 900 912 L 900 1200 Z" fill="var(--leaf-bright)"/>
      <path d="M248 1200 C 420 1045 625 962 900 932 L 900 1200 Z" fill="var(--paper)"/>
      <path d="M248 1200 C 420 1045 625 962 900 932 L 900 1200 Z" fill="url(#lower-sheen)"/>
      <defs>
        <linearGradient id="lower-sheen" x1="0" y1="0" x2="0" y2="1">
          <stop offset="0" stop-color="#ffffff"/>
          <stop offset="1" stop-color="#e4e4e4"/>
        </linearGradient>
      </defs>
    </svg>

    <h1 class="headline headline-main">HUSH AND LOOK</h1>
    <div class="headline-rule"></div>
    <p class="headline headline-sub">THROUGH</p>

    <div class="union-mark">KEU</div>

    <p class="event-name">HALT</p>
    <p class="event-date"><span class="date-blank">XXth</span> OCTOBER</p>
  </main>
</body>
</html>
```